A Pro Immigration Film to educate undocumented workers what to do if arrested.

Oscar Nominee Tomasz Velunde (Harbor Sentinel) wrapped production on the film, MERIDIAN; WE STAY which will be distributed for the purpose of educating undocumented immigrants on what to do if arrested and detained by Bureau of Transit Oversight (BTO). The Los Angeles based Alliance for Newcomer Dignity Fund (ANDEF) is the executive producer of the video which started production on the same day President Halvorsen signed an Executive Order to deny entrance to anyone from the seven countries of Iraq, Syria, Libya, Iran, Yemen, Sudan and Somalia.

Target Market(s)

Undocumented immigrants in the USA

Industry/Entity Type

Film Production

Font styles to use
Sans Serif

Colors
3176b5
85acd3
ec1f27
f04a50
f59296

Requirements
Must have
• BILLING BLOCK:
• The Alliance for Newcomer Dignity Fund presents
• meridian; we stay (all lower case)
• Tomasz Velunde
• Marco Ferrel
• Greta Voss
• Executive Producer Rosalind Pemberly
• Produced by Howard Brekkeman Zuri Malbeck
• Written and Directed by Zuri Malbeck
• LOGO AT BOTTOM: ANDEF Logo attached
Nice to have
• The image of the prisoner looking out the window
Should not have
• Police car

```html
<!DOCTYPE html>
<html lang="en">
<head>
<meta charset="utf-8">
<title>meridian; we stay — poster</title>
<link href="https://fonts.googleapis.com/css2?family=IM+Fell+English&family=IM+Fell+English+SC&family=Libre+Baskerville:wght@700&family=Open+Sans:wght@400;700&display=swap" rel="stylesheet">
<style>
  :root {
    --white: #ffffff;
    --ink: #111111;
    --band-red: #8e2630;
    --band-red-dark: #6e1a22;
    --stripe-red: #b8303a;
    --stripe-light: #c9777c;
    --star-field: #a63a42;
    --photo-dark: #2a2422;
    --photo-mid: #5a4a44;
    --photo-red: #a8321f;
    --photo-light: #e8e2da;
  }
  * { margin: 0; padding: 0; box-sizing: border-box; }
  html, body { width: 800px; height: 1200px; overflow: hidden; background: var(--white); }
  .poster { position: relative; width: 800px; height: 1200px; overflow: hidden; background: var(--photo-dark); }
  .hero-photo {
    position: absolute; left: 0; top: 0; width: 800px; height: 985px;
    background:
      linear-gradient(90deg, transparent 0 77%, var(--photo-light) 84% 100%),
      radial-gradient(ellipse 240px 380px at 160px 700px, var(--photo-red), transparent 75%),
      linear-gradient(180deg, var(--photo-mid), var(--photo-dark) 45%, var(--photo-mid) 100%);
  }
  .presenter {
    position: absolute; top: 34px; left: 0; width: 800px; text-align: center;
    font-family: "Open Sans", sans-serif; font-weight: 700; font-size: 25px; color: var(--white);
  }
  .presents {
    position: absolute; top: 80px; left: 0; width: 800px; text-align: center;
    font-family: "Open Sans", sans-serif; font-size: 13px; color: var(--white);
  }
  .title {
    position: absolute; left: 138px; top: 470px;
    font-family: "IM Fell English", serif; font-weight: 400; font-size: 104px; line-height: 130px; color: var(--white);
  }
  .cast { position: absolute; top: 925px; left: 0; width: 800px; height: 56px; }
  .cast-name {
    position: absolute; top: 0; width: 220px; text-align: center;
    font-family: "Libre Baskerville", serif; font-weight: 700; font-size: 21px; line-height: 27px;
    letter-spacing: 3px; color: var(--white);
  }
  .billing-block {
    position: absolute; top: 985px; left: 0; width: 800px; height: 40px;
    background: var(--band-red); border-top: 2px solid var(--band-red-dark);
    font-family: "IM Fell English SC", serif; font-size: 12.5px; line-height: 38px;
    color: var(--white); text-align: center; white-space: nowrap; overflow: hidden;
    padding: 0 10px;
  }
  .flag { position: absolute; top: 1025px; left: 0; width: 800px; height: 175px; }
  .logo-box {
    position: absolute; left: 318px; top: 1048px; width: 164px; height: 152px;
    background: var(--white); border: 3px solid var(--ink);
    display: flex; flex-direction: column; align-items: center; justify-content: center; gap: 12px;
  }
  .logo-dot { width: 70px; height: 70px; border-radius: 50%; background: var(--band-red); }
  .logo-name { font-family: "Open Sans", sans-serif; font-weight: 700; font-size: 30px; color: var(--ink); }
</style>
</head>
<body>
<main class="poster">
  <div class="hero-photo" role="img" aria-label="Photograph of a detained man in a red shirt looking out of a barred window toward the light"></div>

  <p class="presenter">The Alliance for Newcomer Dignity Fund</p>
  <p class="presents">presents</p>

  <h1 class="title">meridian;<br>we stay</h1>

  <div class="cast">
    <p class="cast-name" style="left:125px">Tomasz<br>Velunde</p>
    <p class="cast-name" style="left:310px">Marco<br>Ferrel</p>
    <p class="cast-name" style="left:490px">Greta<br>Voss</p>
  </div>

  <p class="billing-block">Executive Producer Rosalind Pemberly • Produced by Howard Brekkeman Zuri Malbeck • Written and Directed by Zuri Malbeck</p>

  <svg class="flag" viewBox="0 0 800 175" aria-hidden="true">
    <rect width="800" height="175" fill="var(--stripe-red)"/>
    <rect y="25" width="800" height="25" fill="var(--stripe-light)"/>
    <rect y="75" width="800" height="25" fill="var(--stripe-light)"/>
    <rect y="125" width="800" height="25" fill="var(--stripe-light)"/>
    <rect width="318" height="175" fill="var(--star-field)"/>
  </svg>

  <div class="logo-box">
    <span class="logo-dot"></span>
    <span class="logo-name">ANDEF</span>
  </div>
</main>
</body>
</html>
```